A stationary and business card desgn for a podiatry clinic

i require a stationary design for letter heads, envelopes, buisness cards.

it is for a new podiatry practise within a medical centre, that deals with all lower limb pathology and injury and foot related problems.

the colour scheme for my exisiting logo is orange blue and white. colours provided below.
i would like a white background for the buisness card.

the final design should portray health and wellbeing in a professional manner that still looks modern but sophisticated.

male and female, off all ethinical backgrounds aged between 30-80 years

Medical

• letter head.
need to include all contact details mentioned below.
need to also include ABN 53120978446

i prefer the logo on the top left hand corner and the contact info on the right. the address can be written in a sentence like form as the footer.

Business card
Front:

include logo provided.

clinic details on the front of the card.

Delphine Carrow
B.Pod

P: 7394 5186
F: 7394 5130
M: 0437 612 908
E: delphine@tavrin.com.au
W: www.tavrin.com.au

(may use icons to indicate contact type)

on back

Appointments:

lines to write dates, time etc.
(3-4 of these)
and a small photo of just the foot from the logo in coloured watermark.

Address:
Brackwell Medical Centre
47 Tallowin Street
Brackwell SA 5174
(this location infomation could be in smaller font at the bottom of the buisness card under a line, running in a sentence like fashion) or in the bottom left or right hand corner in a paragraph like you would write it on an envelope

however if you think a different lay out at the back will look better by all means i just need to have room for the appointment even if it is just lines/ space.

i also prefer square cards not rounded corners.

thanks
• plain texts such as times new roman and arial

```html
<!DOCTYPE html>
<html lang="en">
<head>
<meta charset="utf-8">
<title>Tavrin Podiatry – Envelope Set</title>
<link href="https://fonts.googleapis.com/css2?family=PT+Sans:wght@400;700&display=swap" rel="stylesheet">
<style>
  :root {
    --navy-deep: #141f5c;
    --navy: #263a96;
    --navy-bright: #2e47a8;
    --orange: #f26522;
    --paper: #ffffff;
    --ink: #3a3a3a;
    --stage: #ecebe6;
    --edge: #d6d6d6;
  }
  * { margin: 0; padding: 0; box-sizing: border-box; }
  html, body { width: 1200px; height: 739px; overflow: hidden; }
  body {
    background: var(--stage);
    font-family: "PT Sans", Arial, sans-serif;
    position: relative;
  }
  .envelope {
    position: absolute;
    width: 832px;
    height: 372px;
    background: var(--paper);
    border: 1px solid var(--edge);
    overflow: hidden;
  }
  .envelope--back-blue { left: 265px; top: 16px; }
  .envelope--back-white { left: 81px; top: 175px; }
  .envelope--front { left: 169px; top: 339px; }

  .flap { position: absolute; left: 0; top: 0; width: 832px; height: 160px; }

  .flap-brand {
    position: absolute;
    left: 0; width: 832px;
    text-align: center;
    font-weight: 700;
    font-size: 22px;
  }
  .envelope--back-blue .flap-brand { top: 52px; color: var(--paper); }
  .envelope--back-white .flap-brand { top: 60px; color: var(--navy); }

  .brand {
    position: absolute;
    left: 30px; top: 44px;
    display: flex; align-items: center; gap: 10px;
  }
  .brand-dot {
    width: 18px; height: 18px; border-radius: 50%;
    background: var(--orange);
  }
  .brand-name {
    font-weight: 700;
    font-size: 36px;
    line-height: 1;
    color: var(--navy);
  }
  .return-address {
    position: absolute;
    left: 34px; top: 142px;
    font-size: 11px;
    line-height: 15px;
    color: var(--ink);
    font-style: normal;
  }
  .footer-band {
    position: absolute;
    left: 0; bottom: 0;
    width: 100%; height: 35px;
    background: linear-gradient(90deg, var(--navy-deep), var(--navy-bright) 50%, var(--navy-deep));
    display: flex; align-items: center;
    padding-left: 32px;
  }
  .footer-url {
    color: var(--paper);
    font-weight: 700;
    font-size: 10px;
    letter-spacing: 1.5px;
  }
</style>
</head>
<body>

  <section class="envelope envelope--back-blue" aria-label="Envelope back, blue flap">
    <svg class="flap" viewBox="0 0 832 160" aria-hidden="true">
      <defs>
        <linearGradient id="flapBlue" x1="0" x2="1" y1="0" y2="0">
          <stop offset="0" stop-color="#141f5c"/>
          <stop offset="0.5" stop-color="#2e47a8"/>
          <stop offset="1" stop-color="#141f5c"/>
        </linearGradient>
      </defs>
      <path d="M0 0 H832 V40 Q832 92 790 100 L430 140 Q416 142 402 140 L42 100 Q0 92 0 40 Z" fill="url(#flapBlue)"/>
    </svg>
    <div class="flap-brand">Tavrin Podiatry</div>
  </section>

  <section class="envelope envelope--back-white" aria-label="Envelope back, white flap">
    <svg class="flap" viewBox="0 0 832 160" aria-hidden="true">
      <path d="M0 0 Q10 34 40 42 L400 143 Q416 147 432 143 L792 42 Q822 34 832 0" fill="none" stroke="#111" stroke-width="1.2"/>
    </svg>
    <div class="flap-brand">Tavrin Podiatry</div>
  </section>

  <section class="envelope envelope--front" aria-label="Envelope front">
    <div class="brand">
      <span class="brand-dot"></span>
      <span class="brand-name">Tavrin Podiatry</span>
    </div>
    <address class="return-address">
      Brackwell Medical Centre<br>
      47 Tallowin Street<br>
      Brackwell SA 5174
    </address>
    <div class="footer-band">
      <span class="footer-url">www.tavrin.com.au</span>
    </div>
  </section>

</body>
</html>
```